Poster Design Project

We need a poster designed for of range of products, We would like the 7 suitcases on a police line up style wall, maybe a brick style and they are in the spotlight with a heading of The Unusual Suspects.. then smaller maybe along the bottom Not All Luggage Is The Same.. Stand Out From the Crowd..
I have the images of the cases and need this soon, it must be modern and very cool looking. let me know if you have any questions.
Target Market(s)
this is for Ladies 15 - 55 or store owners.
Industry/Entity Type
Crowd
Look and feel

```html
<!DOCTYPE html>
<html lang="en">
<head>
<meta charset="utf-8">
<title>The Unusual Suspects – Luggage Poster</title>
<link rel="stylesheet" href="https://fonts.googleapis.com/css2?family=Damion&family=Righteous&display=swap">
<style>
  :root {
    --wall-top: #7d4a40;
    --wall-bottom: #8e5a4c;
    --floor-top: #5f4a37;
    --floor-bottom: #3f2f22;
    --title-white: #ffffff;
    --title-shadow: #3a1512;
    --stroke-green: #3f6b1f;
    --tagline-yellow: #f2c21e;
    --case-green: #9bd43a;
    --case-white: #eceef1;
    --case-yellow: #f1ae17;
    --case-city: #3b3b3b;
    --case-grey: #b9b9b9;
    --case-blue: #a8cfe6;
    --case-pink: #e26cc0;
    --case-name: #8a8f92;
    --wheel: #2a2a2a;
  }
  html, body {
    margin: 0;
    padding: 0;
    overflow: hidden;
    background: #222;
  }
  .poster {
    position: relative;
    width: 1200px;
    height: 849px;
    overflow: hidden;
  }
  .wall {
    position: absolute;
    left: 0; top: 0;
    width: 1200px; height: 605px;
    background: linear-gradient(180deg, var(--wall-top), var(--wall-bottom));
  }
  .floor {
    position: absolute;
    left: 0; top: 605px;
    width: 1200px; height: 244px;
    background: linear-gradient(180deg, var(--floor-top), var(--floor-bottom));
  }
  .brush-stroke {
    position: absolute;
    left: 230px; top: 110px;
    width: 650px; height: 240px;
  }
  .headline {
    position: absolute;
    left: 0; top: 50px;
    width: 1200px;
    margin: 0;
    text-align: center;
    font-family: "Damion", cursive;
    font-weight: 400;
    font-size: 120px;
    line-height: 104px;
    color: var(--title-white);
    text-shadow: 5px 5px 0 var(--title-shadow);
    transform: rotate(-4deg);
  }
  .headline span { display: block; }
  .headline .line-the { margin-left: -30px; }
  .headline .line-unusual { margin-left: -20px; }
  .headline .line-suspects { margin-left: 30px; }

  .case {
    position: absolute;
    border-radius: 14px;
    box-shadow: inset -6px 0 12px rgba(0,0,0,0.18), 0 6px 10px rgba(0,0,0,0.35);
  }
  .case::before, .case::after {
    content: "";
    position: absolute;
    bottom: -16px;
    width: 14px; height: 16px;
    border-radius: 4px;
    background: var(--wheel);
  }
  .case::before { left: 12px; }
  .case::after { right: 12px; }
  .case-name {
    position: absolute;
    left: 0; top: 66px;
    width: 100%;
    text-align: center;
    font-family: "Righteous", sans-serif;
    font-size: 15px;
    letter-spacing: 4px;
    color: var(--case-name);
  }
  .case-green  { left: 62px;  top: 372px; width: 172px; height: 292px; background: var(--case-green); }
  .case-yellow { left: 293px; top: 402px; width: 160px; height: 262px; background: linear-gradient(160deg, var(--case-yellow), #c98510); }
  .case-washer { left: 192px; top: 494px; width: 128px; height: 208px; background: var(--case-white); }
  .case-blue   { left: 786px; top: 370px; width: 172px; height: 292px; background: var(--case-blue); }
  .case-pink   { left: 986px; top: 403px; width: 160px; height: 262px; background: linear-gradient(160deg, var(--case-pink), #5a2a4c); }
  .case-city   { left: 478px; top: 456px; width: 180px; height: 290px; background: linear-gradient(160deg, #555, var(--case-city) 60%, #1c1c1c); }
  .case-grey   { left: 682px; top: 484px; width: 160px; height: 262px; background: linear-gradient(160deg, #eeeeee, var(--case-grey) 55%, #3a3a3a); }

  .tagline {
    position: absolute;
    left: 0; top: 785px;
    width: 1200px;
    margin: 0;
    text-align: center;
    font-family: "Righteous", sans-serif;
    font-size: 30px;
    line-height: 36px;
    color: var(--tagline-yellow);
  }
</style>
</head>
<body>
  <main class="poster">
    <div class="wall" role="img" aria-label="Red brick wall backdrop"></div>
    <div class="floor" role="img" aria-label="Weathered wooden plank floor"></div>

    <svg class="brush-stroke" viewBox="0 0 650 240" role="img" aria-label="Green painted brush stroke behind the heading">
      <polygon points="20,20 300,40 300,60 20,50" fill="var(--stroke-green)" opacity="0.45"/>
      <polygon points="100,150 620,10 640,40 150,200" fill="var(--stroke-green)" opacity="0.85"/>
      <polygon points="110,220 560,150 580,175 120,235" fill="var(--stroke-green)" opacity="0.6"/>
    </svg>

    <h1 class="headline">
      <span class="line-the">The</span>
      <span class="line-unusual">Unusual</span>
      <span class="line-suspects">Suspects</span>
    </h1>

    <div class="case case-green" role="img" aria-label="Lime green hard-shell suitcase">
      <span class="case-name">VELOQUIN</span>
    </div>
    <div class="case case-yellow" role="img" aria-label="Yellow suitcase printed with an Eiffel Tower photo"></div>
    <div class="case case-washer" role="img" aria-label="White suitcase printed as a washing machine"></div>
    <div class="case case-blue" role="img" aria-label="Pale blue hard-shell suitcase">
      <span class="case-name">VELOQUIN</span>
    </div>
    <div class="case case-pink" role="img" aria-label="Pink suitcase printed with an Eiffel Tower photo"></div>
    <div class="case case-city" role="img" aria-label="Black and white suitcase printed with a city street collage"></div>
    <div class="case case-grey" role="img" aria-label="Black and white suitcase printed with an Eiffel Tower photo"></div>

    <p class="tagline">not all luggage is the same... stand out from the crowd</p>
  </main>
</body>
</html>
```